Anzeige zur Kundenakquise
Zielgruppe
Wir sind der größte unabhängige Versicherungsmakler Deutschlands.
https://www.vendler-tarifkreis.de/
Aufgabenstellung
Die Anzeige dient zur Kundenakquise. Der Flyer soll in erster Linie auf Trivolo veröffentlicht werden.
Sie soll Kunden anregen eine Nachricht an uns zu schicken und einen Termin bis zum 30.11.2018 zu vereinbaren um ihre KFZ-Versicherungen vergleichen zu lassen.
Der alte Flyer wird mit hochgeladen. Bitte den Text nicht 1 zu 1 übernehmen.
Farbe und Stil sollten übernommen werden.
Die Maße für Trivolo:
Empfohlene Bildgröße:
1.200 x 628 Pixel
Bildseitenverhältnis: 1,91:1
Auf Grund der Zusendung von mehrerern Flyer der Designer bitte ich die Anzahl auf 3 zu einigen, d.h. bitte senden Sie für eine Trivolo Slidekampane 3 Flyer als ein Projekt zu. Vielen Dank für Ihre Mühe.

```html
<!DOCTYPE html>
<html lang="de">
<head>
<meta charset="utf-8">
<title>Vendler Tarifkreis – KFZ-Versicherung vergleichen</title>
<link href="https://fonts.googleapis.com/css2?family=Source+Sans+3:ital,wght@0,300;0,400;0,700;1,700&display=swap" rel="stylesheet">
<style>
  :root {
    --slate: #545454;
    --lime: #9dc41f;
    --lime-deep: #87a926;
    --white: #ffffff;
    --haze: #f8efe0;
    --gold: #e8b67c;
    --amber: #c98a52;
    --field: #b9a47e;
    --car-dark: #35363b;
  }
  * { margin: 0; padding: 0; box-sizing: border-box; }
  html, body { width: 1200px; height: 628px; overflow: hidden; background: var(--white); }
  body { font-family: "Source Sans 3", sans-serif; }

  .ad {
    position: relative;
    width: 1200px;
    height: 628px;
    overflow: hidden;
  }
  .ad__photo {
    position: absolute;
    inset: 0;
    background:
      linear-gradient(168deg, rgba(0,0,0,0) 72%, rgba(53,54,59,0.75) 84%, var(--car-dark) 96%),
      linear-gradient(205deg, rgba(0,0,0,0) 55%, rgba(53,54,59,0.55) 70%, rgba(53,54,59,0) 78%),
      radial-gradient(ellipse 260px 200px at 300px 430px, rgba(201,138,82,0.55), rgba(201,138,82,0)),
      radial-gradient(ellipse 300px 220px at 700px 460px, rgba(232,182,124,0.7), rgba(232,182,124,0)),
      radial-gradient(ellipse 220px 200px at 860px 450px, rgba(201,138,82,0.45), rgba(201,138,82,0)),
      linear-gradient(180deg, var(--haze) 30%, #efdcc0 46%, var(--field) 52%, var(--gold) 64%, var(--amber) 80%);
  }
  .ad__header {
    position: absolute;
    top: 0; left: 0;
    width: 1200px;
    height: 139px;
    background: var(--slate);
  }
  .ad__headline {
    position: absolute;
    top: 30px; left: 0;
    width: 1200px;
    text-align: center;
    color: var(--white);
    font-weight: 400;
    font-size: 42px;
    letter-spacing: 0.3px;
    white-space: nowrap;
  }
  .ad__claim {
    position: absolute;
    top: 95px; left: 0;
    width: 723px; height: 44px;
    background: var(--lime);
    color: var(--white);
    font-weight: 300;
    font-size: 32px;
    line-height: 44px;
    padding-left: 53px;
    white-space: nowrap;
  }
  .ad__cta {
    position: absolute;
    top: 139px; left: 477px;
    width: 723px; height: 43px;
    background: var(--lime-deep);
    color: var(--white);
    font-weight: 700;
    font-style: italic;
    font-size: 30px;
    line-height: 43px;
    padding-left: 20px;
    white-space: nowrap;
  }
  .badge {
    position: absolute;
    border-radius: 50%;
    background: var(--white);
    box-shadow: 0 2px 8px rgba(0,0,0,0.15);
    display: flex;
    align-items: center;
    justify-content: center;
  }
  .badge--brand {
    left: 38px; top: 200px;
    width: 130px; height: 130px;
    gap: 6px;
  }
  .brand__mark {
    width: 12px; height: 12px;
    background: var(--lime);
  }
  .brand__name {
    color: var(--lime);
    font-weight: 700;
    font-size: 15px;
    line-height: 1.1;
    letter-spacing: 0.3px;
  }
  .badge--icon { left: 1039px; width: 104px; height: 104px; }
  .badge--car { top: 217px; }
  .badge--money { top: 355px; }
  .badge--travel { top: 494px; }
  .badge svg { width: 76px; height: 76px; }

  .ad__url {
    position: absolute;
    left: 40px; top: 568px;
    color: var(--white);
    font-weight: 700;
    font-size: 31px;
    letter-spacing: 0.3px;
  }
</style>
</head>
<body>
<main class="ad">
  <div class="ad__photo" role="img" aria-label="Sonniges Foto: fröhliche Freundinnen mit Sonnenhüten fahren mit erhobenen Armen in einem dunklen Cabrio über Land"></div>

  <header class="ad__header">
    <h1 class="ad__headline">IHR ERSPARTES GELD GEHÖRT IN DEN NÄCHSTEN URLAUB!</h1>
  </header>
  <p class="ad__claim">Wir finden Ihre günstigste KFZ-Versicherung</p>
  <p class="ad__cta">Schreiben Sie uns – Termin bis zum 30.11.2018</p>

  <div class="badge badge--brand">
    <span class="brand__mark"></span>
    <span class="brand__name">VENDLER<br>TARIFKREIS</span>
  </div>

  <div class="badge badge--icon badge--car">
    <svg viewBox="0 0 76 76" aria-hidden="true">
      <path d="M4 44 L8 36 L28 34 L36 38 L60 36 L72 40 L72 46 L4 46 Z" fill="var(--lime)"/>
      <path d="M48 36 Q54 24 62 28" fill="none" stroke="var(--lime)" stroke-width="3"/>
      <circle cx="18" cy="47" r="6" fill="var(--lime)" stroke="var(--white)" stroke-width="2"/>
      <circle cx="58" cy="47" r="6" fill="var(--lime)" stroke="var(--white)" stroke-width="2"/>
    </svg>
  </div>

  <div class="badge badge--icon badge--money">
    <svg viewBox="0 0 76 76" aria-hidden="true" fill="var(--white)" stroke="var(--lime)" stroke-width="3" stroke-linejoin="round">
      <path d="M14 30 L50 14 L60 36 L24 52 Z"/>
      <path d="M12 38 L48 22 L58 44 L22 60 Z"/>
      <path d="M10 46 L46 30 L56 52 L20 68 Z"/>
      <circle cx="33" cy="49" r="5"/>
    </svg>
  </div>

  <div class="badge badge--icon badge--travel">
    <svg viewBox="0 0 76 76" aria-hidden="true">
      <path d="M34 66 Q36 44 32 28" fill="none" stroke="var(--lime)" stroke-width="4" stroke-linecap="round"/>
      <path d="M32 28 Q20 18 8 24 Q20 24 32 28 Q26 14 36 8 Q34 20 32 28 Q44 16 56 22 Q42 22 32 28 Q46 28 50 40 Q40 30 32 28 Q20 32 16 44 Q22 32 32 28 Z" fill="var(--lime)"/>
      <path d="M56 66 Q58 54 56 44" fill="none" stroke="var(--lime)" stroke-width="3" stroke-linecap="round"/>
      <path d="M56 44 Q48 38 42 42 Q50 42 56 44 Q56 34 64 32 Q60 38 56 44 Q66 40 70 48 Q62 44 56 44 Z" fill="var(--lime)"/>
      <path d="M20 70 H68" stroke="var(--lime)" stroke-width="3" stroke-linecap="round"/>
    </svg>
  </div>

  <p class="ad__url">www.vendler-tarifkreis.de</p>
</main>
</body>
</html>
```